Clear Plastic Card Design

I am looking to have a business card designed from my logo icon. I am looking to match the style of a different business card I have attached in the files.
Looking for a card that is plastic, with layers of transparency in the shape of my logo icon (also attached in the files) - not a circle like the other card. The winning design will incorporate the red icon logo on the front and back and include the charity's name, "Lanterns for the Weary" in the same or similar font, as well as an email and phone number. For now, use the email: email@lanternsfortheweary.org and the phone number 555-318-4072.
We like how the sample business card has transparency, partial and full opacity layers and a matching color scheme. Files will need to be in vector so that our business card printing company can work with it.
UPDATE:
We've some excellent designs in, thank you everyone! I got an early review from the owner, and he requested a minor redirect to find his perfect design. He wants the design to stand out by NOT being a rectangle. Try instead a circle, square, or best yet - something that falls in the outline of the logo icon, either fully or partially. Thank you, everyone!
Contact Information for Business Card
Lanterns for the Weary text should be incorporated as well as a phone and email.
Look and feel

```html
<!DOCTYPE html>
<html lang="en">
<head>
<meta charset="utf-8">
<title>Lanterns for the Weary – Business Card</title>
<link rel="stylesheet" href="https://fonts.googleapis.com/css2?family=Montserrat:wght@300;700&family=Lexend:wght@400&display=swap">
<style>
  :root {
    --page-bg: #e6e9ec;
    --frost-light: #f6f7f9;
    --frost-mid: #e4e7eb;
    --crimson: #c41d3a;
    --brick: #b8322a;
    --ember: #d45a1c;
    --orange-line: #e0621e;
    --ink: #1a1a1a;
    --card-text: #f4f1f0;
  }
  * { margin: 0; padding: 0; box-sizing: border-box; }
  html, body {
    width: 1200px;
    height: 1008px;
    overflow: hidden;
    background: var(--page-bg);
  }
  .card {
    position: absolute;
    left: 200px;
    top: 104px;
    width: 800px;
    height: 800px;
    border-radius: 40px;
    overflow: hidden;
    box-shadow: 0 10px 30px rgba(0,0,0,0.12);
  }
  .card-art {
    position: absolute;
    inset: 0;
    width: 800px;
    height: 800px;
  }
  .brand {
    position: absolute;
    right: 236px;
    top: 204px;
    text-align: right;
    font-family: "Lexend", sans-serif;
    font-weight: 400;
    font-size: 37px;
    line-height: 1.2;
    color: var(--ink);
  }
  .brand-mark {
    position: absolute;
    left: 590px;
    top: 96px;
    width: 150px;
    height: 150px;
    background: var(--crimson);
  }
  .holder-name {
    position: absolute;
    left: 68px;
    top: 562px;
    font-family: "Montserrat", sans-serif;
    font-weight: 700;
    font-size: 40px;
    letter-spacing: 0.5px;
    color: var(--card-text);
  }
  .contact-list {
    position: absolute;
    left: 68px;
    top: 632px;
    list-style: none;
    font-family: "Montserrat", sans-serif;
    font-weight: 300;
    font-size: 28px;
    color: var(--card-text);
  }
  .contact-item {
    display: flex;
    align-items: center;
    gap: 10px;
    height: 46px;
  }
  .contact-icon { width: 26px; height: 22px; flex: none; }
  .envelope-flap { stroke: var(--brick); }
</style>
</head>
<body>
  <main class="card">
    <svg class="card-art" viewBox="0 0 800 800">
      <defs>
        <linearGradient id="frost" x1="0" y1="0" x2="1" y2="1">
          <stop offset="0" stop-color="var(--frost-light)"/>
          <stop offset="1" stop-color="var(--frost-mid)"/>
        </linearGradient>
        <linearGradient id="ember-band" x1="0" y1="0" x2="1" y2="0">
          <stop offset="0" stop-color="var(--crimson)"/>
          <stop offset="0.55" stop-color="var(--brick)"/>
          <stop offset="1" stop-color="var(--ember)"/>
        </linearGradient>
        <linearGradient id="accent-fade" x1="0" y1="0" x2="1" y2="0">
          <stop offset="0" stop-color="var(--crimson)"/>
          <stop offset="1" stop-color="var(--orange-line)"/>
        </linearGradient>
      </defs>
      <rect class="frost-field" width="800" height="800" fill="url(#frost)" role="img" aria-label="Frosted low-poly faceted texture across the upper card"/>
      <path class="accent-line" d="M0,302 C200,300 330,404 470,462 C590,510 700,490 800,484" fill="none" stroke="url(#accent-fade)" stroke-width="5"/>
      <path class="accent-black" d="M0,322 C210,320 340,432 480,490 C600,536 700,528 800,528" fill="none" stroke="var(--ink)" stroke-width="14"/>
      <path class="lower-band" d="M0,344 C210,344 340,452 480,506 C600,550 700,546 800,544 L800,800 L0,800 Z" fill="url(#ember-band)"/>
    </svg>

    <div class="brand-mark"></div>
    <h1 class="brand">Lanterns for the<br>Weary</h1>

    <p class="holder-name">DANIEL WHITFORD</p>
    <ul class="contact-list">
      <li class="contact-item">
        <svg class="contact-icon" viewBox="0 0 26 22"><path d="M2,8 C2,3 24,3 24,8 L24,10 L18,10 L18,7 L8,7 L8,10 L2,10 Z M6,11 L20,11 L24,20 L2,20 Z" fill="currentColor"/></svg>
        <span>555-318-4072</span>
      </li>
      <li class="contact-item">
        <svg class="contact-icon" viewBox="0 0 26 22"><rect x="1" y="4" width="24" height="15" fill="currentColor"/><path class="envelope-flap" d="M1,4 L13,13 L25,4" fill="none" stroke-width="2"/></svg>
        <span>email@lanternsfortheweary.org</span>
      </li>
    </ul>
  </main>
</body>
</html>
```